Business Card Design Project

Looking for a logo and business card for a Real State Business i will be opening. The name is not choosen yet , but will probably be RTV IMOVEIS.
I was thinking black and silver colors, but am open to nice ideas.
I did add a business card that i liked a lot, am looking for something like that, with logo in black or silver in a black card. The logo i was thinking in the letters RTV as i uploaded or something or little and cute buildings or a house...just ideas, can be any nice logo.
Updates

You guys can add other colors if you want, I like colors very "BRIGHT" and "open", like red, pink, strong colors. almost glow in the dark colors. lol

Designers,

I've increased more 88 dollars in the budget for 1st place cause I will want envelope designs... small and big sizes.

So 1st place is now U$248,00. 

No need to send the envelope designs right now... only the business cards designs.

Thank you.

Industry/Entity Type

Business

Requirements
Must have
• Renata Tavares Vilela

www.RTVimoveis-exemplo.com.br

+554188316402

renata@rtvimoveis-exemplo.com.br

```html
<!DOCTYPE html>
<html lang="pt-BR">
<head>
<meta charset="utf-8">
<title>RTV Imoveis – Business Cards</title>
<link rel="stylesheet" href="https://fonts.googleapis.com/css2?family=Arimo:wght@400;700&display=swap">
<style>
  :root {
    --backdrop: #1c1c1d;
    --card-dark: #2c2b2d;
    --glow-red: #e8192a;
    --glow-deep: #7a1419;
    --band-dark: #140306;
    --silver-light: #ffffff;
    --silver-mid: #c9c9c9;
    --silver-dark: #7d7d7d;
    --ink: #0b0b0b;
    --brand-maroon: #2a0a0d;
    --text-white: #ffffff;
  }
  * { margin: 0; padding: 0; box-sizing: border-box; }
  html, body {
    width: 1200px;
    height: 929px;
    overflow: hidden;
    background: var(--backdrop);
    font-family: "Arimo", Arial, sans-serif;
  }
  .stage {
    position: relative;
    width: 1200px;
    height: 929px;
  }
  .card {
    position: absolute;
    left: 300px;
    width: 600px;
    height: 360px;
    box-shadow: 0 10px 30px rgba(0, 0, 0, 0.6);
  }
  .card--back { top: 80px; }
  .card--front { top: 489px; }
  .card svg { display: block; width: 600px; height: 360px; }
  .brand-mark { font-family: "Arimo", Arial, sans-serif; font-weight: 700; fill: var(--ink); }
  .brand-word { font-family: "Arimo", Arial, sans-serif; font-weight: 400; fill: var(--brand-maroon); }
  .site-url { font-family: "Arimo", Arial, sans-serif; font-weight: 400; fill: var(--text-white); }
  .contact-line { font-family: "Arimo", Arial, sans-serif; font-weight: 400; fill: var(--ink); }
</style>
</head>
<body>
<main class="stage">

  <!-- Card back: brand side -->
  <section class="card card--back" aria-label="RTV Imoveis card, brand side">
    <svg viewBox="0 0 600 360" xmlns="http://www.w3.org/2000/svg">
      <defs>
        <radialGradient id="back-glow" cx="0.47" cy="0.62" r="0.55">
          <stop offset="0" stop-color="var(--glow-red)"/>
          <stop offset="0.45" stop-color="var(--glow-deep)"/>
          <stop offset="1" stop-color="var(--card-dark)"/>
        </radialGradient>
        <linearGradient id="back-silver" x1="0" y1="1" x2="1" y2="0">
          <stop offset="0" stop-color="var(--silver-light)"/>
          <stop offset="0.55" stop-color="var(--silver-mid)"/>
          <stop offset="1" stop-color="var(--silver-dark)"/>
        </linearGradient>
      </defs>
      <rect class="card-base" width="600" height="360" fill="url(#back-glow)"/>
      <polygon class="silver-panel" points="0,312 600,132 600,360 0,360" fill="url(#back-silver)"/>
      <polygon class="dark-band" points="0,290 600,110 600,134 0,314" fill="var(--band-dark)"/>
      <text class="site-url" x="0" y="0" font-size="15"
            transform="translate(305 245) rotate(-16.7)">www.RTVimoveis-exemplo.com.br</text>
      <rect class="brand-square" x="188" y="112" width="22" height="22" fill="var(--ink)"/>
      <text class="brand-mark" x="220" y="148" font-size="58">RTV</text>
    </svg>
  </section>

  <!-- Card front: contact side -->
  <section class="card card--front" aria-label="RTV Imoveis card, contact side">
    <svg viewBox="0 0 600 360" xmlns="http://www.w3.org/2000/svg">
      <defs>
        <radialGradient id="front-glow" cx="0.55" cy="0.52" r="0.55">
          <stop offset="0" stop-color="var(--glow-red)"/>
          <stop offset="0.45" stop-color="var(--glow-deep)"/>
          <stop offset="1" stop-color="var(--card-dark)"/>
        </radialGradient>
        <linearGradient id="arc-sheen" x1="0" y1="0" x2="1" y2="0">
          <stop offset="0" stop-color="var(--ink)"/>
          <stop offset="0.5" stop-color="var(--silver-mid)"/>
          <stop offset="0.8" stop-color="var(--ink)"/>
          <stop offset="1" stop-color="var(--ink)"/>
        </linearGradient>
        <linearGradient id="front-silver" x1="0" y1="0" x2="1" y2="0">
          <stop offset="0" stop-color="var(--silver-light)"/>
          <stop offset="0.6" stop-color="var(--silver-mid)"/>
          <stop offset="1" stop-color="var(--silver-dark)"/>
        </linearGradient>
        <clipPath id="front-clip"><rect width="600" height="360"/></clipPath>
      </defs>
      <rect class="card-base" width="600" height="360" fill="url(#front-glow)"/>
      <g clip-path="url(#front-clip)">
        <ellipse class="swoosh-arc" cx="250" cy="70" rx="330" ry="145"
                 fill="none" stroke="url(#arc-sheen)" stroke-width="18"/>
      </g>
      <rect class="dark-band" x="0" y="235" width="600" height="26" fill="var(--band-dark)"/>
      <rect class="silver-panel" x="0" y="261" width="600" height="99" fill="url(#front-silver)"/>

      <rect class="brand-square" x="112" y="52" width="10" height="10" fill="var(--ink)"/>
      <text class="brand-mark" x="126" y="80" font-size="30">RTV</text>
      <text class="brand-word" x="88" y="124" font-size="27">IMOVEIS</text>

      <rect class="brand-square" x="440" y="98" width="14" height="14" fill="var(--ink)"/>
      <text class="brand-mark" x="460" y="140" font-size="44">RTV</text>

      <text class="contact-line" x="34" y="296" font-size="15">Name:Renata Tavares Vilela</text>
      <text class="contact-line" x="34" y="317" font-size="15">Email:renata@rtvimoveis-exemplo.com.br</text>
      <text class="contact-line" x="34" y="338" font-size="15">Number:+554188316402</text>
    </svg>
  </section>

</main>
</body>
</html>
```